Roots of Harvest Brochure Design Project

We need a brochure that we can use to promote our education not-for-profit, Roots of Harvest Fund (www.rootsofharvest.org) and promote our African bracelets that we are selling to fundraise for our organisation. The target audience is from high school to 40 years in the US and Australia.
Updates

Please find below the link to a new hi res logo. Thanks!
https://www.filevault.example/s/8qm27rtlop31zzwe/Roots_of_Harvest_logo_NEW.ai
https://www.filevault.example/sh/4kd91wqp58hbx3/QRMVPEZuo7

Reason: We have decided the final design to choose. Please give us a week to finalise.

Industry/Entity Type

High School

Requirements
Must have
• Photos of bracelets
Roots of Harvest logo
emotive photos of African students
A4 size with fold out features

```html
<!DOCTYPE html>
<html lang="en">
<head>
<meta charset="utf-8">
<title>Roots of Harvest : Inside</title>
<link rel="stylesheet" href="https://fonts.googleapis.com/css2?family=Open+Sans:ital,wdth,wght@0,75..100,300..800;1,75..100,300..800&display=swap">
<style>
  :root {
    --earth: #47403a;
    --leaf: #22cc11;
    --paper: #ffffff;
    --ink: #1c1c1c;
    --marker: #e01010;
    --rule: #222222;
  }
  * { box-sizing: border-box; margin: 0; padding: 0; }
  html, body { width: 1200px; height: 900px; overflow: hidden; background: var(--paper); }
  body { position: relative; font-family: "Open Sans", Arial, sans-serif; color: var(--ink); }

  .sheet-title {
    position: absolute; left: 0; width: 1064px; top: 16px; text-align: center;
    font-size: 20px; font-weight: 600; color: #333;
  }
  .fold-label {
    position: absolute; left: 836px; top: 2px; width: 20px; height: 100px;
    writing-mode: vertical-rl; color: var(--marker); font-size: 13px; font-weight: 600;
  }
  .fold-tick { position: absolute; width: 1px; height: 24px; background: var(--rule); }

  .sheet {
    position: absolute; left: 75px; top: 108px; width: 1050px; height: 741px;
    border: 1px solid var(--rule);
  }
  .band { position: absolute; }
  .band--top { left: 5px; top: 9px; width: 778px; height: 9px; background: var(--earth); }
  .band--leaf-top { left: 787px; top: 9px; width: 256px; height: 10px; background: var(--leaf); }
  .band--leaf-bottom { left: 787px; top: 708px; width: 256px; height: 24px; background: var(--leaf); }
  .band--donate {
    left: 10px; top: 709px; width: 773px; height: 26px; background: var(--earth);
    color: var(--paper); font-weight: 700; font-size: 17px; font-stretch: 90%;
    text-align: right; padding-right: 24px; line-height: 26px;
  }

  .brand {
    position: absolute; left: 10px; top: 60px; width: 300px; height: 350px;
    display: flex; flex-direction: column; align-items: center; justify-content: center; gap: 22px;
  }
  .brand__dot { width: 110px; height: 110px; border-radius: 50%; background: var(--leaf); }
  .brand__name {
    font-size: 46px; line-height: 1.02; font-weight: 800; color: var(--earth);
    text-align: center; text-transform: uppercase;
  }

  .heading {
    position: absolute; background: var(--leaf); color: var(--earth);
    font-size: 14px; font-weight: 700; padding-left: 6px; width: 153px; height: 25px; line-height: 25px;
  }
  .column {
    position: absolute; width: 237px; font-size: 12.4px; line-height: 17.3px;
    font-stretch: 85%; text-align: justify; hyphens: auto;
  }
  .column p + p { margin-top: 17px; }

  .help-panel {
    position: absolute; left: 787px; top: 28px; width: 256px; height: 676px; background: var(--earth);
    color: var(--paper); text-align: center;
  }
  .help-panel__title { margin-top: 92px; font-size: 25px; font-weight: 700; font-stretch: 90%; }
  .help-panel__title em { font-style: normal; color: var(--leaf); }
  .help-panel__call { margin-top: 28px; font-size: 16.5px; line-height: 28px; font-weight: 700; font-stretch: 90%; }
  .help-panel__photo {
    position: absolute; left: 13px; top: 237px; width: 233px; height: 226px;
    background: radial-gradient(ellipse at 55% 50%, #b88a6a 0%, #8a7566 35%, #c9c9c9 75%);
  }
  .help-panel__legend {
    position: absolute; left: 14px; top: 484px; width: 232px; height: 96px;
    border: 3px solid var(--paper); text-align: left; padding: 12px 0 0 4px;
    font-size: 10.6px; line-height: 21px; font-stretch: 85%;
  }
  .help-panel__legend b { font-style: italic; }
</style>
</head>
<body>
  <div class="sheet-title">Roots of Harvest : Inside</div>
  <div class="fold-label">fold markers</div>
  <div class="fold-tick" style="left:336px;top:79px"></div>
  <div class="fold-tick" style="left:858px;top:79px"></div>
  <div class="fold-tick" style="left:336px;top:853px"></div>
  <div class="fold-tick" style="left:858px;top:853px"></div>

  <main class="sheet">
    <div class="band band--top"></div>
    <div class="band band--leaf-top"></div>

    <div class="brand">
      <div class="brand__dot"></div>
      <div class="brand__name">Roots of Harvest Fund</div>
    </div>

    <h2 class="heading" style="left:7px;top:424px">Who we are</h2>
    <div class="column" style="left:12px;top:462px">
      <p>In 2009, we launched Roots of Harvest Fund with a humble goal of providing brilliant but economically disadvantaged students in Zimbabwe at least a decent shot of achieving their dreams. Over the past four years, we have provided academic scholarships supported over 60 students in two provinces and five different schools, including 20 primary school students. An overwhelming majority of our students were orphaned by the AIDS pandemic or political violence or general lack of access to adequate health services and Roots of Harvest became their one and only hope of continuing their education.</p>
    </div>
    <div class="column" style="left:272px;top:462px">
      <p>Roots of Harvest Fund continues to be dedicated to supporting, sustaining and promoting education through the provision of essential education resources for students in under-resourced Zimbabwean communities through generosity of our supporters around the world.</p>
      <p>Roots of Harvest Inc., is registered and incorporated in the states of New York, USA and New South Wales, Australia. Roots of Harvest has US 501(c)(3) Federal Tax-Exempt Status.</p>
    </div>

    <h2 class="heading" style="left:524px;top:124px">Our philosophy</h2>
    <div class="column" style="left:534px;top:160px">
      <p>We subscribe to the philosophy of development through education – the idea that education is the most powerful and effective way to bring change, independence, innovation, and prosperity. Fundamentally, the belief is that education can serve towards ending aspects of poverty, bringing enlightenment, and transforming individual lives and communities.</p>
      <p>Roots of Harvest strives to be part of the effort to create the next generation of educated African who are independent thinkers and innovators. We aim to instill the spirit of giving back within the students and ensure that they will contribute to the future growth and prosperity of Zimbabwe and Africa at large.</p>
    </div>

    <h2 class="heading" style="left:524px;top:480px">The Need</h2>
    <div class="column" style="left:534px;top:514px">
      <p>For every student we have helped, we have turned down at least five other motivated, intelligent and desperate students who we cannot help due financial constraints. We more of our students are finishing high school and graduating from our program, we reaching out to our supporters to help us recruit more students into the Roots of Harvest Scholarship Program and give them and their families a chance at life.</p>
    </div>

    <aside class="help-panel">
      <h2 class="help-panel__title">How you can <em>help!</em></h2>
      <p class="help-panel__call">BUY, SELL OR PROMOTE<br>the Roots of Harvest Bracelets.</p>
      <div class="help-panel__photo" role="img" aria-label="Photo of three leather bracelets with beaded details"></div>
      <div class="help-panel__legend">
        <div><b>One bracelet</b> = One Month of school for one child</div>
        <div><b>Three bracelets</b> = One Term of school for one child</div>
        <div><b>Nine bracelets</b> = One year of school for one child</div>
      </div>
    </aside>

    <div class="band band--leaf-bottom"></div>
    <div class="band band--donate">Donate to Roots of Harvest Fund at www.rootsofharvest.org</div>
  </main>
</body>
</html>
```